Ridgeline pedal treks co

we are an electric mountain bike company in Nelson, New Zealand. We need to create flyers to have in local stores/ information centres etc for our company. you can view the website for ideas on whats required in the flyer www. ridgelinepedaltreksco.example.nz., on the website in our region and our trails gives me detail on the tracks etc available to the clients. I will attach in the brief some screen shots from the website of the content on our services packages etc . I Will also upload a couple versions of our logo.If you wish to incorporate anything else that represents nz and the Nelson region that would be fantastic. Please include all relevant contact email, facebook, instagram etc, looking for something with flare that catches the eye but also clarity on information and looks appealing. wanting DLE size double sided

Target Market(s)

international travellers/ staff parties/ group bookings/

Industry/Entity Type

Tourism

Requirements
Must have
• 1. map of nz with nelson on it. Location
• 2 info on or services
• 3. contact info
• 4. about the region
• 5. track information.
• 6 tour information.
• 7. eye catching layout.
Nice to have
• 1. information on what we offer.
• 2. nz icons etc kiwi, silver fern, southern alps, marlow reach, scenery shots

```html
<!DOCTYPE html>
<html lang="en">
<head>
<meta charset="utf-8">
<title>Ridgeline Pedal Treks Co – DL Flyer</title>
<link href="https://fonts.googleapis.com/css2?family=Bebas+Neue&family=Fira+Sans+Condensed:ital,wght@0,500;1,500;1,600&family=PT+Sans:ital,wght@0,400;0,700;1,400&display=swap" rel="stylesheet">
<style>
:root{
  --green:#3cb54a;
  --green-dark:#1f7d2e;
  --ink:#111;
  --charcoal:#2a2a2a;
  --grey-text:#555;
  --muted:#777;
  --white:#fff;
  --bg:#e9e9e9;
}
*{box-sizing:border-box;margin:0;padding:0}
html,body{width:1200px;height:1139px;overflow:hidden;background:var(--bg)}
body{position:relative;font-family:"PT Sans",sans-serif}
.flyer{position:absolute;top:60px;width:472px;height:992px;background:var(--white);overflow:hidden;box-shadow:0 2px 8px rgba(0,0,0,.25)}
.flyer--front{left:102px}
.flyer--back{left:640px}
.abs{position:absolute}

/* front */
.front__title{top:30px;left:0;width:100%;text-align:center;font-family:"Bebas Neue",sans-serif;font-size:42px;color:var(--ink);letter-spacing:.5px}
.front__tagline{top:84px;left:0;width:100%;text-align:center;font-family:"PT Sans",sans-serif;font-weight:700;font-size:21px;color:var(--green)}
.front__photo{top:122px;left:0;width:100%;height:440px;background:linear-gradient(180deg,#b9cbd8 0%,#5f7890 22%,#3a4a3e 55%,#2b2f28 100%)}
.front__dark{top:0;left:0;width:100%;height:100%}
.front__headline{top:610px;left:20px;width:432px;text-align:center;font-size:26px;line-height:29px;color:var(--green)}
.front__rule{top:686px;left:24px;width:424px;height:1px;background:var(--green)}
.front__copy{left:14px;width:444px;text-align:center;font-size:14.5px;line-height:17.6px;color:#eee}
.copy-1{top:712px}
.copy-2{top:800px}

/* brand mark */
.brand{display:flex;align-items:center;justify-content:center;border-radius:50%;background:var(--ink);border:6px solid var(--white);text-align:center;font-family:"PT Sans",sans-serif;font-weight:700;color:var(--white);box-shadow:0 0 0 2px var(--ink)}

/* booking bar */
.book{top:900px;left:0;width:100%;height:50px;background:var(--green);display:flex;align-items:center;justify-content:center;gap:14px;font-family:"Bebas Neue",sans-serif;font-size:38px;color:var(--white);padding-top:3px}
.book svg{width:32px;height:32px}
.web{top:950px;left:0;width:100%;height:42px;background:var(--ink);color:var(--white);text-align:center;font-size:17px;line-height:38px}

/* back */
.back__map{top:0;left:0;width:100%;height:300px;background:linear-gradient(160deg,#9dc4d6 0%,#c9d8b4 40%,#e5dcc0 70%,#c8d9a8 100%)}
.back__title{top:326px;left:0;width:100%;text-align:center;font-family:"Bebas Neue",sans-serif;font-size:46px;color:var(--ink)}
.ribbon{left:0;height:28px;background:var(--green);color:var(--white);font-family:"Fira Sans Condensed",sans-serif;font-style:italic;font-weight:500;font-size:18px;line-height:28px;padding-left:22px;border-radius:0 14px 14px 0;box-shadow:0 2px 3px rgba(0,0,0,.25)}
.list{left:22px;list-style:none;font-size:14.5px;color:#333}
.list li{height:18.3px;line-height:18.3px;display:flex;align-items:center;white-space:nowrap}
.list li::before{content:"";width:11px;height:11px;border-radius:50%;background:var(--green);margin-right:8px;flex:none;background-image:linear-gradient(45deg,transparent 45%,#fff 45%,#fff 60%,transparent 60%)}
.level{font-family:"Fira Sans Condensed",sans-serif;font-style:italic;font-size:12px;color:var(--muted);margin-left:3px}
.price{width:70px;height:70px;border-radius:50%;background:var(--green);color:var(--white);display:flex;align-items:center;justify-content:center;text-align:center;font-family:"Bebas Neue",sans-serif;font-size:16px;line-height:16px;box-shadow:0 0 0 3px rgba(60,181,74,.35)}
.back__wave{top:740px;left:0;width:100%;height:160px}
.quote{top:832px;left:22px;width:440px;display:flex;gap:12px;color:var(--white)}
.quote__mark{font-family:"Bebas Neue",sans-serif;font-size:64px;line-height:50px;color:var(--green)}
.quote p{font-style:italic;font-size:14px;line-height:18.5px}
</style>
</head>
<body>

<!-- FRONT -->
<section class="flyer flyer--front">
  <div class="abs front__photo" role="img" aria-label="Photo of four riders standing with electric mountain bikes on a hilltop above Nelson and the bay"></div>
  <div class="abs" style="top:0;left:0;width:100%;height:150px;background:linear-gradient(180deg,#fff 65%,rgba(255,255,255,0))"></div>
  <h1 class="abs front__title">RIDGELINE PEDAL TREKS CO</h1>
  <p class="abs front__tagline">TRAVEL FURTHER AND FASTER</p>

  <svg class="abs front__dark" viewBox="0 0 472 992" preserveAspectRatio="none" aria-hidden="true">
    <defs>
      <linearGradient id="darkFront" x1="0" y1="0" x2="0" y2="1">
        <stop offset="0" stop-color="#4a4a4a"/><stop offset=".5" stop-color="#1e1e1e"/><stop offset="1" stop-color="#0c0c0c"/>
      </linearGradient>
    </defs>
    <path d="M0 500 C120 590 300 560 472 460 L472 992 L0 992Z" fill="var(--green)"/>
    <path d="M0 510 C120 600 300 575 472 478 L472 992 L0 992Z" fill="var(--green-dark)"/>
    <path d="M0 530 C120 610 300 590 472 500 L472 992 L0 992Z" fill="#fff"/>
    <path d="M0 542 C130 622 300 605 472 512 L472 992 L0 992Z" fill="url(#darkFront)"/>
  </svg>

  <div class="abs brand" style="left:288px;top:402px;width:172px;height:172px;font-size:21px;line-height:24px">Ridgeline<br>Pedal<br>Treks Co</div>

  <h2 class="abs front__headline" style="font-weight:400">Exploring our world class trails in the Nelson &amp; Tasman region</h2>
  <div class="abs front__rule"></div>
  <p class="abs front__copy copy-1">Explore Sunny Nelson’ is the oldest city in the South Island of New Zealand and the home of beautiful beaches and trails, national parks, plenty of sunshine, amazing cafes and eaterys and a variety of accommodation options to suit every budget.</p>
  <p class="abs front__copy copy-2">One of the best things about our region is that you don’t have to travel far to find world class outdoor activities, one of which is our mountain biking scene.</p>

  <div class="abs book">BOOK NOW
    <svg viewBox="0 0 32 32" aria-hidden="true"><circle cx="16" cy="16" r="14" fill="none" stroke="#fff" stroke-width="2.5"/><path d="M11 9c1-1 2-1 2.6 0l1.6 2.6c.5.8.2 1.6-.5 2.1l-.9.6c.8 1.8 2.2 3.3 4 4.2l.7-.9c.5-.7 1.3-.9 2.1-.4l2.5 1.6c.9.6.9 1.6 0 2.6-1.3 1.4-3 1.8-5 .8-3.7-1.9-6.5-4.8-8.2-8.5-.8-1.9-.3-3.6 1.1-4.7z" fill="#fff"/></svg>
    +64 210 555 0147</div>
  <p class="abs web">www.ridgelinepedaltreksco.example.nz</p>
</section>

<!-- BACK -->
<section class="flyer flyer--back">
  <div class="abs back__map" role="img" aria-label="Road and trail map of Nelson and Tasman Bay with trail areas marked in green"></div>
  <svg class="abs" style="top:0;left:0" width="472" height="330" viewBox="0 0 472 330" aria-hidden="true">
    <path d="M0 272 C110 330 260 330 472 218 L472 330 L0 330Z" fill="var(--green)"/>
    <path d="M0 288 C110 340 270 330 472 236 L472 330 L0 330Z" fill="#fff"/>
  </svg>
  <div class="abs brand" style="left:304px;top:174px;width:146px;height:146px;font-size:18px;line-height:21px">Ridgeline<br>Pedal<br>Treks Co</div>

  <h2 class="abs back__title" style="font-weight:400">WHAT WE OFFER</h2>

  <div class="abs ribbon" style="top:380px;width:218px">E-BIKE RENTAL</div>
  <ul class="abs list" style="top:411px">
    <li>Half-Full day rental</li>
    <li>Trailcraft Full Suspension Vero Comp</li>
    <li>Add on shuttle and airport transfers available</li>
  </ul>
  <div class="abs price" style="left:385px;top:395px">FROM $119<br>TO $189</div>

  <div class="abs ribbon" style="top:478px;width:218px">GUIDED E-BIKE TOURS</div>
  <ul class="abs list" style="top:513px">
    <li>Kaiteriteri MTB Park and Marlow Reach<span class="level">- Beginner/Intermediate</span></li>
    <li>Rameka Trail Golden Bay<span class="level">- Intermediate/Advanced</span></li>
    <li>Coppermine/Third house<span class="level">- Beginner/Intermediate</span></li>
    <li>Nelson Lakes<span class="level">- Beginner/Intermediate/Advanced</span></li>
    <li>Codgers MTB park/Fringe Hill<span class="level">- Beginner/Intermediate/Advanced</span></li>
    <li>Barnicoat/Involution<span class="level">- Intermediate/Advanced</span></li>
    <li>Richmond Hills<span class="level">- Intermediate/Advanced</span></li>
    <li>Sharlands<span class="level">- Beginner/Intermediate/Advanced</span></li>
  </ul>
  <div class="abs price" style="left:385px;top:591px">START FROM<br>$209PP</div>

  <div class="abs ribbon" style="top:676px;width:218px">ULTIMATE MTB GETAWAY</div>
  <ul class="abs list" style="top:705px">
    <li>3 day Scenic Adventure Tour<span class="level">- Beginner/Intermediate</span></li>
    <li>3 day Adrenaline Fueled Tour<span class="level">- Intermediate/Advanced</span></li>
  </ul>
  <div class="abs price" style="left:385px;top:675px">PRICE ON<br>ENQUIRY</div>

  <svg class="abs back__wave" viewBox="0 0 472 160" preserveAspectRatio="none" aria-hidden="true">
    <defs>
      <linearGradient id="darkBack" x1="0" y1="0" x2="0" y2="1">
        <stop offset="0" stop-color="#3a3a3a"/><stop offset="1" stop-color="#111"/>
      </linearGradient>
    </defs>
    <path d="M0 8 C150 -6 300 40 472 90 L472 160 L0 160Z" fill="var(--green)"/>
    <path d="M0 14 C150 2 300 48 472 98 L472 160 L0 160Z" fill="#fff"/>
    <path d="M0 20 C160 10 300 58 472 110 L472 160 L0 160Z" fill="url(#darkBack)"/>
    <path d="M260 72 C340 88 410 70 472 40 L472 78 C400 100 330 98 260 72Z" fill="var(--green-dark)"/>
  </svg>
  <div class="abs" style="top:880px;left:0;width:100%;height:20px;background:#111"></div>

  <div class="abs quote">
    <span class="quote__mark">“</span>
    <p>Great trails and top notch equipment.<br>For a nnovice like mzself zour excellent tips and tricks reallz made the daz amaying” - Dana Holt</p>
  </div>

  <div class="abs book">BOOK NOW
    <svg viewBox="0 0 32 32" aria-hidden="true"><circle cx="16" cy="16" r="14" fill="none" stroke="#fff" stroke-width="2.5"/><path d="M11 9c1-1 2-1 2.6 0l1.6 2.6c.5.8.2 1.6-.5 2.1l-.9.6c.8 1.8 2.2 3.3 4 4.2l.7-.9c.5-.7 1.3-.9 2.1-.4l2.5 1.6c.9.6.9 1.6 0 2.6-1.3 1.4-3 1.8-5 .8-3.7-1.9-6.5-4.8-8.2-8.5-.8-1.9-.3-3.6 1.1-4.7z" fill="#fff"/></svg>
    +64 210 555 0147</div>
  <p class="abs web">www.ridgelinepedaltreksco.example.nz</p>
</section>

</body>
</html>
```